Wordpress Site Design for a Horror and Action Movie Production Company

We need a re-design/facelift of our website: https://q7zk.pagecraftr-demo.net
The structure of the website could remain the same, but it needs to look and feel BETTER!

We would like the website coded in Wordpress so that it can be easily updated bu us, via adding new projects and new projects' info.

We specialize in Action, Horror, and Sci-Fi Genre. That being said, we don't want the website to look like it's a themed park with haunted houses. It should still be sharp and professional, as after all - it is a business for us!

Target Market(s)

Film Distribution Companies (B2B), as well as general audience that likes movies

Industry/Entity Type

Movie Production

Coding

Coded - Design and coding required

Number of Pages Required

5+ page

Font styles to use
Sans Serif

Colors

Designer to choose colors to be used in the design.

Requirements
Must have
• - PROJECTS page
• - Each PROJECT has a sub-page with project info/updates (up dates could be in a form of a WP post, ideally a template that we can use to update and create new PROJECT pages, with text, poster, and video link (trailer))
• - NEWS page that chronologically lists updates from all PROJECTS (could be done via WP blog)
• - HOME page would
Nice to have
• Should generally have a dark background.
• Websites we like as a reference of general approach and style:
• https://marlowvexla.com
• https://tuvakreel.com (however this is very image-centric, and we might not have that much imagery at the moment)
• https://www.pebblecreeklightandframe.com/other
• https://kelvapics.com
Should not have
• We specialize in Action, Horror, and Sci-Fi Genre. That being said, we don't want the website to look like it's a themed park with haunted houses. It should still be sharp and professional, as after all - it is a business for us!

```html
<!DOCTYPE html>
<html lang="en">
<head>
<meta charset="utf-8">
<title>Bunker 42 Media</title>
<link rel="stylesheet" href="https://fonts.googleapis.com/css2?family=Playfair+Display:wght@400;700&family=Rubik:wght@400;500&display=swap">
<style>
:root{
  --ink:#1f1c1d;
  --bg:#262223;
  --bg-alt:#2b2728;
  --card:#343031;
  --orange:#ff6a00;
  --white:#ffffff;
  --text:#d9d6d7;
  --muted:#8f8b8c;
  --soft-blue:#9aa3b5;
  --link-blue:#7f9ad1;
  --line:#4a4546;
}
*{box-sizing:border-box;margin:0;padding:0}
html,body{width:1200px;height:4802px;overflow:hidden;background:var(--bg)}
body{font-family:'Rubik',sans-serif;color:var(--text)}
section,header,footer{position:relative;width:1200px;overflow:hidden}
.abs{position:absolute}
.serif{font-family:'Playfair Display',serif;font-weight:700;color:var(--white)}

/* header */
.site-header{height:106px;background:var(--ink)}
.brand{left:194px;top:32px;font-size:25px;font-weight:500;color:var(--white);letter-spacing:1px}
.brand-sub{display:block;font-size:10px;letter-spacing:5px;margin-top:2px;text-align:center}
.main-nav{left:622px;top:46px;display:flex;gap:33px;font-size:11px;color:var(--white);letter-spacing:.3px}
.search-icon{left:994px;top:44px}

.hero{height:606px;background:linear-gradient(100deg,#e6e6e6 0%,#9a9a9a 38%,#3f3f3f 62%,#bdbdbd 100%)}
.hero-media{inset:0}

/* about + projects */
.about-projects{height:1425px;background:var(--bg)}
.about-title{left:200px;top:160px;width:216px;text-align:center;font-size:44px;line-height:50px}
.about-text{left:472px;top:93px;width:552px;font-size:15.5px;line-height:26px;letter-spacing:.5px;color:var(--soft-blue)}
.about-text p+p{margin-top:14px}
.about-rule{left:320px;top:430px;width:560px;height:1px;background:var(--line)}
.eyebrow{font-size:10.5px;color:var(--orange);letter-spacing:.5px;display:flex;align-items:center;gap:10px;justify-content:center}
.eyebrow::before,.eyebrow::after{content:"";width:22px;height:1px;background:var(--orange)}
.eyebrow.left{justify-content:flex-start}
.eyebrow.left::before{display:none}
.projects-label{left:0;width:1200px;top:546px}
.section-title{left:0;width:1200px;text-align:center;font-size:44px;line-height:48px}
.projects-title{top:580px}
.project{overflow:hidden}
.project .poster{position:absolute;inset:0}
.play{position:absolute;width:40px;height:40px;border-radius:50%;background:var(--orange);left:50%;top:50%;transform:translate(-50%,-50%)}
.play::after{content:"";position:absolute;left:16px;top:12px;border-left:12px solid #fff;border-top:8px solid transparent;border-bottom:8px solid transparent}
.project-name{position:absolute;left:0;right:0;text-align:center;font-family:'Playfair Display',serif;font-weight:700;color:#fff;font-size:21px}
.p1{left:52px;top:726px;width:257px;height:257px}
.p2{left:332px;top:726px;width:257px;height:257px}
.p3{left:52px;top:1002px;width:537px;height:240px}
.p4{left:611px;top:726px;width:537px;height:516px}
.btn{left:522px;top:1285px;width:156px;height:41px;border-radius:21px;background:var(--orange);color:#fff;font-size:12.5px;font-weight:500;display:flex;align-items:center;justify-content:center;gap:8px}

/* partners */
.partners{height:589px;background:linear-gradient(180deg,#3a3637,#2c2829 60%,#332f30)}
.partners-label{left:0;width:1200px;top:104px}
.partners-title{top:132px}
.partner-card{top:276px;width:203px;height:236px;background:#fff;color:#333}
.partner-head{height:66px;display:flex;align-items:center;gap:14px;border-bottom:1px solid #e5e5e5}
.headshot{width:74px;height:66px;background:linear-gradient(135deg,#9b9b9b,#4e4e4e)}
.partner-name{font-size:15px;color:#222}
.partner-bio{padding:12px 8px 0 8px;font-size:10.5px;line-height:17px;color:#444}
.card-go{position:absolute;right:16px;bottom:20px;width:23px;height:23px;border-radius:50%;background:var(--orange)}
.slider-arrow{width:45px;height:45px;border-radius:50%;background:var(--orange);top:373px}

/* history */
.history{height:823px;background:var(--bg)}
.history-label{left:0;width:1200px;top:100px}
.history-title{top:126px}
.history-intro{left:0;width:1200px;top:266px;text-align:center;font-size:13.5px;line-height:26px;color:var(--link-blue)}
.timeline{left:380px;top:376px;width:438px;height:1px;background:var(--line)}
.dot{width:45px;height:45px;border-radius:50%;background:#3b3738;top:354px;display:flex;align-items:center;justify-content:center}
.dot.small{width:26px;height:26px;top:364px}
.history-card{top:458px;width:404px;height:296px;background:var(--card);padding:30px 22px}
.history-card::before{content:"";position:absolute;left:188px;top:-14px;border-bottom:14px solid var(--card);border-left:14px solid transparent;border-right:14px solid transparent}
.history-card h3{font-family:'Playfair Display',serif;font-weight:400;font-size:17px;color:#fff;text-align:center}
.history-card p{margin-top:14px;font-size:10.5px;line-height:19px;color:var(--muted);text-align:justify}
.badge{position:absolute;right:12px;bottom:30px;width:96px;height:56px;background:#1d1a1b}
.badge.light{background:#ffffff;width:100px;height:42px}

/* news */
.news{height:549px;background:var(--bg)}
.news-label{left:171px;top:70px}
.news-title{left:171px;top:96px;font-size:44px;line-height:46px}
.news-list{left:194px;top:226px;width:256px;list-style:none}
.news-list li{font-size:11px;line-height:17px;color:var(--link-blue);padding:10px 0 18px;border-bottom:1px solid var(--line)}
.news-list li+li{color:var(--muted)}
.news-list li:last-child{border-bottom:none}
.round-btn{width:42px;height:42px;border-radius:50%;border:2px solid #d0d0d0;top:473px}
.news-photo{left:538px;top:54px;width:488px;height:341px;background:linear-gradient(160deg,#5a4a3a,#2a211b 60%,#6b1a18)}
.news-caption{left:538px;top:395px;width:488px;height:99px;background:#fff;padding:18px 24px}
.news-caption h4{font-family:'Playfair Display',serif;font-weight:400;font-size:18px;line-height:22px;color:#222}
.news-meta{margin-top:12px;font-size:10.5px;color:#888;display:flex;gap:22px}

/* instagram */
.instagram{height:382px;background:#fff}
.insta-title{left:0;width:1200px;top:44px;text-align:center;color:#111;font-size:44px}
.insta-row{left:0;top:155px;width:1200px;height:214px;display:flex}
.insta-row div{flex:1}

/* footer */
.site-footer{height:322px;background:var(--ink)}
.footer-brand{left:0;width:1200px;top:54px;text-align:center;font-size:32px;font-weight:500;color:#fff;letter-spacing:1px}
.footer-brand .brand-sub{font-size:12px;letter-spacing:6px}
.footer-rule{left:500px;top:132px;width:200px;height:1px;background:#888}
.social{left:0;width:1200px;top:178px;display:flex;justify-content:center;gap:26px}
.social span{width:18px;height:18px;border-radius:50%;background:#fff}
.copyright{left:0;width:1200px;top:246px;text-align:center;font-size:10.5px;color:#fff}
</style>
</head>
<body>

<header class="site-header">
  <div class="abs brand">BUNKER 42<span class="brand-sub">MEDIA</span></div>
  <nav class="abs main-nav"><span>HOME</span><span>ABOUT</span><span>PROJECTS</span><span>NEWS</span><span>CONTACT</span></nav>
  <svg class="abs search-icon" width="14" height="14" viewBox="0 0 14 14"><circle cx="6" cy="6" r="4.5" fill="none" stroke="#fff" stroke-width="1.8"/><line x1="9.3" y1="9.3" x2="13" y2="13" stroke="#fff" stroke-width="1.8"/></svg>
</header>

<section class="hero">
  <div class="abs hero-media" role="img" aria-label="Black and white photo of a camera operator filming with a cinema camera rig"></div>
</section>

<section class="about-projects">
  <h2 class="abs serif about-title">About<br>Us</h2>
  <div class="abs about-text">
    <p>Bunker 42 Media Inc (B42M) is a fresh brand of multi-media Visual Content, aimed at development of original Canadian content as well as servicing of foreign productions here at home, in Ontario, Canada.</p>
    <p>We produce genre feature films, series, documentaries, and anything else that we feel great about. We take pride in our innovative approach to the process of filmmaking and marketing of our produced content. In simple terms, we make good looking motion picture content that is entertaining, visually compelling, and tells a good story.</p>
  </div>
  <div class="abs about-rule"></div>

  <div class="abs eyebrow projects-label">PROJECTS</div>
  <h2 class="abs serif section-title projects-title">Our<br>Latest Projects</h2>

  <div class="abs project p1">
    <div class="poster" role="img" aria-label="Poster still for Dark Harbor in warm amber tones" style="background:linear-gradient(135deg,#c98a3e,#6b3a17 60%,#2a1508)"></div>
    <div class="play"></div><div class="project-name" style="top:170px">Dark Harbor</div>
  </div>
  <div class="abs project p2">
    <div class="poster" role="img" aria-label="Poster still for Nitro Boy with two riders in helmets" style="background:linear-gradient(135deg,#8fa3b8,#b9533d 50%,#5e6e7a)"></div>
    <div class="play"></div><div class="project-name" style="top:170px">Nitro Boy</div>
  </div>
  <div class="abs project p3">
    <div class="poster" role="img" aria-label="Poster still for Pushed Too Far showing an action scene" style="background:linear-gradient(135deg,#4a4a3e,#8a7d6a 55%,#3b3a33)"></div>
    <div class="play"></div><div class="project-name" style="top:150px">Pushed Too Far</div>
  </div>
  <div class="abs project p4">
    <div class="poster" role="img" aria-label="Poster for Shattered Road: a figure in a red rain-soaked alley" style="background:linear-gradient(90deg,#151515 0%,#2a2a2a 30%,#c41a1a 48%,#9a1111 58%,#262626 75%,#141414 100%)"></div>
    <div class="play"></div><div class="project-name" style="top:462px">Shattered Road</div>
  </div>

  <div class="abs btn">View all projects
    <svg width="12" height="8" viewBox="0 0 12 8"><path d="M0 4h10M7 1l3 3-3 3" stroke="#fff" stroke-width="1.5" fill="none"/></svg>
  </div>
</section>

<section class="partners">
  <div class="abs eyebrow partners-label">OUR PARTNERS</div>
  <h2 class="abs serif section-title partners-title">We Have Got Many<br>Talented Partners</h2>

  <div class="abs slider-arrow" style="left:85px"><svg width="45" height="45" viewBox="0 0 45 45"><path d="M25 17l-5 5.5 5 5.5" stroke="#fff" stroke-width="1.6" fill="none"/></svg></div>
  <div class="abs slider-arrow" style="left:1071px"><svg width="45" height="45" viewBox="0 0 45 45"><path d="M20 17l5 5.5-5 5.5" stroke="#fff" stroke-width="1.6" fill="none"/></svg></div>

  <article class="abs partner-card" style="left:160px">
    <div class="partner-head"><div class="headshot" role="img" aria-label="Portrait of Dorian Vale"></div><span class="partner-name">Dorian Vale</span></div>
    <p class="partner-bio">Dorian Vale is an award-winning Writer/Producer/Director with over 15 years experience in the film and television industry...</p>
    <span class="card-go"></span>
  </article>
  <article class="abs partner-card" style="left:386px">
    <div class="partner-head"><div class="headshot" role="img" aria-label="Portrait of Milo Varenko"></div><span class="partner-name">Milo Varenko</span></div>
    <p class="partner-bio">Milo Varenko is a 18-year-long veteran of the film biz. Starting out as a cinematographer, he developed a unique visual style ...</p>
    <span class="card-go"></span>
  </article>
  <article class="abs partner-card" style="left:611px">
    <div class="partner-head"><div class="headshot" role="img" aria-label="Portrait of Owen Brask"></div><span class="partner-name">Owen Brask</span></div>
    <p class="partner-bio">Owen Brask has taken a decidedly different path to the film industry than his partners have. A successful entrepreneur ...</p>
    <span class="card-go"></span>
  </article>
  <article class="abs partner-card" style="left:829px">
    <div class="partner-head"><div class="headshot" role="img" aria-label="Portrait of Victor Lenz"></div><span class="partner-name">Victor Lenz</span></div>
    <p class="partner-bio">With more than 10 years experience in the field of international distribution, Victor Lenz is one of the most respected names in the area of independent film....</p>
    <span class="card-go"></span>
  </article>
</section>

<section class="history">
  <div class="abs eyebrow history-label">OUR HISTORY</div>
  <h2 class="abs serif section-title history-title">How Our Brand<br>Was Formed</h2>
  <p class="abs history-intro">B42M is a child of a partnership between two Canadian companies, which for years have been<br>recognized as key brands in the Canadian media landscape</p>

  <div class="abs timeline"></div>
  <div class="abs dot" style="left:357px"><svg width="10" height="12" viewBox="0 0 10 12"><path d="M5 0v10M1 6l4 4 4-4" stroke="#ff6a00" stroke-width="1.5" fill="none"/></svg></div>
  <div class="abs dot small" style="left:587px"><svg width="8" height="8" viewBox="0 0 8 8"><path d="M2 0l4 4-4 4" stroke="#ff6a00" stroke-width="1.3" fill="none"/></svg></div>
  <div class="abs dot" style="left:796px"><svg width="10" height="12" viewBox="0 0 10 12"><path d="M5 0v10M1 6l4 4 4-4" stroke="#ff6a00" stroke-width="1.5" fill="none"/></svg></div>

  <article class="abs history-card" style="left:179px">
    <h3>Crow Ridge Entertainment Inc</h3>
    <p>Crow Ridge Entertainment is led by partners Victor Lenz, Dorian Vale and Owen Brask. It represents unique, innovative and cutting edge genre films for North American distribution and the international marketplace. Through its expertise in strategic project management, Crow Ridge Entertainment can assist in any and all stages of project production. From acquisitions, representation, negotiations, strategic marketing plans, consultation, and sales, Crow Ridge Entertainment is there in whatever capacity needed.</p>
    <div class="badge" role="img" aria-label="Partner badge"></div>
  </article>
  <article class="abs history-card" style="left:617px">
    <h3>Nine Lantern Entertainment Inc</h3>
    <p>Nine Lantern Entertainment is founded by Milo Varenko CEO in 2015, and has since quickly gained momentum. It has been the name behind the production of a feature film Pushed Too Far, a festival darling feature Shattered Road, a number of short films, web series pilots, and is currently in development of a number of original projects.</p>
    <div class="badge light" role="img" aria-label="Partner badge"></div>
  </article>
</section>

<section class="news">
  <div class="abs eyebrow left news-label">NEWS</div>
  <h2 class="abs serif news-title">Our Latest<br>News</h2>
  <ul class="abs news-list">
    <li>Reel Ledger: Crow Ridge partners on production arm, Bunker 42 Media</li>
    <li>Frame Beat: Crow Ridge partners on production arm</li>
    <li>Crow Ridge pacts with Nine Lantern, Blue Quarter (Clipframe subscription required)</li>
  </ul>
  <div class="abs round-btn" style="left:199px"><svg width="38" height="38" viewBox="0 0 38 38"><path d="M21 15l-4 4 4 4" stroke="#fff" stroke-width="1.5" fill="none"/></svg></div>
  <div class="abs round-btn" style="left:248px"><svg width="38" height="38" viewBox="0 0 38 38"><path d="M17 15l4 4-4 4" stroke="#fff" stroke-width="1.5" fill="none"/></svg></div>

  <div class="abs news-photo" role="img" aria-label="Film still of an actor in a period military uniform with a red scarf"></div>
  <div class="abs news-caption">
    <h4>Reel Ledger: Crow Ridge partners on<br>production arm, Bunker 42 Media</h4>
    <div class="news-meta"><span>By Corbin Ashby</span><span>12 Sep, 2017</span></div>
  </div>
</section>

<section class="instagram">
  <h2 class="abs serif insta-title">Instagram</h2>
  <div class="abs insta-row">
    <div role="img" aria-label="Equipment van photo" style="background:linear-gradient(135deg,#2f3b52,#8a8f99)"></div>
    <div role="img" aria-label="Crew member with camera" style="background:linear-gradient(135deg,#3c5f86,#1f2a35)"></div>
    <div role="img" aria-label="On-set scene" style="background:linear-gradient(135deg,#7a8d6e,#2e3a2c)"></div>
    <div role="img" aria-label="Crew on location" style="background:linear-gradient(135deg,#c9c9c9,#3a3a3a)"></div>
    <div role="img" aria-label="Camera rig on set" style="background:linear-gradient(135deg,#dcdcdc,#555)"></div>
    <div role="img" aria-label="Group photo of the crew" style="background:linear-gradient(135deg,#5b3a5e,#201820)"></div>
    <div role="img" aria-label="Bridal costume photo" style="background:linear-gradient(135deg,#e8d8cc,#8a6a55)"></div>
    <div role="img" aria-label="Boat on the shore" style="background:linear-gradient(135deg,#7fa4c8,#3a5a6c)"></div>
    <div role="img" aria-label="Camera equipment close-up" style="background:linear-gradient(135deg,#3a3a3a,#111)"></div>
  </div>
</section>

<footer class="site-footer">
  <div class="abs footer-brand">BUNKER 42<span class="brand-sub">MEDIA</span></div>
  <div class="abs footer-rule"></div>
  <div class="abs social" aria-label="Social links"><span></span><span></span><span></span><span></span></div>
  <p class="abs copyright">©2018 Bunker 42 Media Inc. All rights reserved | Script &amp; Story Submission Notice</p>
</footer>

</body>
</html>
```